Income Tax and Accounting Brochure

I need a brochure using my new logo (file attached). I do tax work and accounting work. I am an EA (QDX Enrolled Agent - logo attached) and would like this incorporated into the brochure. I also have a MSA in Accounting. Please incorporate the text that I have provided in the brochure.

Target Market(s)

Tax Clients - both business and individuals

Industry/Entity Type

Accounting

Colors
0054AA
0677BA
7BADD7
CADEEF
E8F1F8

Requirements
Must have
• Use my logo and the QDX EA file in the brochure
Nice to have
• I would like to see a brochure that I can customize with my own text if possible.

```html
<!DOCTYPE html>
<html lang="en">
<head>
<meta charset="utf-8">
<title>Bluecrest Accounting &amp; Consulting – Tax Brochure</title>
<link href="https://fonts.googleapis.com/css2?family=Lato:ital,wght@0,400;0,700;0,900;1,400;1,700&family=Roboto:wght@500;700&display=swap" rel="stylesheet">
<style>
  :root{
    --blue:#0054aa;
    --blue-deep:#0a3f8c;
    --blue-mid:#0677ba;
    --blue-soft:#7badd7;
    --blue-pale:#cadeef;
    --blue-mist:#e8f1f8;
    --red:#c8202f;
    --ink:#3a3a3a;
    --white:#ffffff;
    --page:#eef0f2;
  }
  *{margin:0;padding:0;box-sizing:border-box}
  html,body{width:902px;height:1200px;overflow:hidden;background:var(--page)}
  body{font-family:"Lato",Arial,sans-serif;color:var(--ink);position:relative}

  .spread{position:absolute;left:51px;width:800px;height:570px;background:var(--white);overflow:hidden;box-shadow:0 2px 8px rgba(0,0,0,.18)}
  .spread--outside{top:20px}
  .spread--inside{top:610px}

  .panel{position:absolute;top:0;width:266.67px;height:570px}
  .panel--1{left:0}
  .panel--2{left:266.67px}
  .panel--3{left:533.33px}

  .photo{position:absolute}
  .swooshes{position:absolute;left:0;top:0;width:800px;height:570px;pointer-events:none}
  .layer{position:absolute;z-index:2}

  .heading{font-family:"Roboto",Arial,sans-serif;font-weight:700;line-height:1.1}
  .body-copy{font-size:8.6px;line-height:1.35;color:var(--ink)}
  .body-copy p+p{margin-top:9px}

  .brand{display:flex;align-items:center;gap:8px}
  .brand__dot{width:34px;height:34px;border-radius:50%;flex:none}
  .brand__name{font-family:"Lato",Arial,sans-serif;font-weight:700;font-size:13px;line-height:1.15;letter-spacing:.5px}

  /* outside spread */
  .about{left:22px;top:178px;width:228px}
  .about__title{font-size:16px;color:var(--blue)}
  .about__title span{color:var(--red)}
  .about__sub{font-family:"Roboto",Arial,sans-serif;font-weight:500;font-size:12px;color:var(--blue);margin:2px 0 8px}
  .quote{left:24px;top:400px;width:140px;font-style:italic;font-weight:700;font-size:14.5px;line-height:1.3;color:var(--blue)}

  .brand--cover{left:322px;top:212px}
  .brand--cover .brand__dot{background:var(--white)}
  .brand--cover .brand__name{color:var(--white)}

  .contacts{left:266.67px;top:390px;width:266.67px;text-align:center;color:var(--white);font-size:10px;line-height:1.3}
  .contact{display:flex;flex-direction:column;align-items:center;margin-bottom:6px}
  .contact svg{width:13px;height:13px;margin-bottom:3px}

  .brand--front{left:560px;top:26px}
  .brand--front .brand__dot{background:var(--red)}
  .brand--front .brand__name{color:var(--blue)}

  .badge{left:595px;top:383px;width:150px;height:40px;border:3px solid var(--blue-soft);background:var(--blue-mist)}
  .cta{left:533.33px;top:440px;width:266.67px;text-align:center}
  .cta__title{font-size:22px;color:var(--blue);letter-spacing:.3px}
  .cta__bar{display:inline-block;margin-top:6px;background:var(--red);color:var(--white);font-family:"Roboto",Arial,sans-serif;font-weight:500;font-size:12.5px;padding:5px 10px}
  .web{font-family:"Lato",Arial,sans-serif;font-weight:700;font-size:11.5px;letter-spacing:1.6px;color:#333}
  .cta .web{margin-top:9px}

  /* inside spread */
  .why{left:25px;top:308px;width:225px}
  .why__title{font-size:17px;color:var(--red);margin-bottom:16px}
  .why__title span{color:var(--blue)}

  .mess-header{left:266.67px;top:0;width:266.67px;height:92px;background:var(--blue);padding:26px 22px 0}
  .mess-header .heading{color:var(--white);font-size:16.5px}
  .mess{left:288px;top:105px;width:228px}
  .mess__lead{font-style:italic;font-weight:700;font-size:10.5px;line-height:1.3;color:#222}
  .mess__title{font-size:19px;color:var(--red);margin:6px 0 8px}

  .gets{left:533.33px;top:0;width:266.67px;padding:26px 22px 0 22px}
  .gets__title{color:var(--white);font-size:16.5px;margin-bottom:20px}
  .gets ul{list-style:none}
  .gets li{position:relative;padding-left:14px;color:var(--white);font-style:italic;font-weight:700;font-size:8.9px;line-height:1.33;margin-bottom:11px}
  .gets li::before{content:"";position:absolute;left:0;top:4px;width:6px;height:6px;border-radius:50%;background:var(--white)}

  .brand--back{left:556px;top:458px}
  .brand--back .brand__dot{background:var(--red)}
  .brand--back .brand__name{color:var(--blue)}
  .web--back{left:533.33px;top:516px;width:266.67px;text-align:center}
</style>
</head>
<body>

<!-- Outside spread -->
<section class="spread spread--outside">
  <div class="panel panel--1">
    <div class="photo" role="img" aria-label="Photo of an advisor shaking hands with a smiling senior couple" style="left:0;top:0;width:266.67px;height:165px;background:linear-gradient(135deg,#e9edf2 0%,#c9d3de 45%,#8aa0b8 100%)"></div>
  </div>
  <div class="panel panel--2" role="img" aria-label="Faint office desk photo under a blue tint" style="background:linear-gradient(160deg,#1d5fb6 0%,var(--blue) 45%,#0a4a9c 100%)"></div>
  <div class="panel panel--3">
    <div class="photo" role="img" aria-label="Photo of hands using a calculator over charts and paperwork" style="left:0;top:75px;width:266.67px;height:250px;background:linear-gradient(135deg,#f3f5f7 0%,#d8dee6 50%,#9fb0c4 100%)"></div>
  </div>

  <svg class="swooshes" viewBox="0 0 800 570" aria-hidden="true">
    <path d="M300,405 C450,330 600,300 800,292 L800,330 C600,334 450,352 300,425 Z" fill="#0054aa"/>
    <path d="M0,540 C150,478 320,368 800,338 L800,354 C430,366 270,440 200,570 L0,570 Z" fill="#ffffff"/>
    <path d="M0,548 C150,486 320,375 800,345 L800,357 C430,370 275,445 210,570 L0,570 Z" fill="#c8202f"/>
    <line x1="266.67" y1="0" x2="266.67" y2="570" stroke="rgba(0,0,0,.06)"/>
    <line x1="533.33" y1="0" x2="533.33" y2="570" stroke="rgba(0,0,0,.06)"/>
  </svg>

  <div class="layer about">
    <h2 class="heading about__title"><span>ABOUT</span> MARIAN D HOLLOWAY,</h2>
    <p class="about__sub">MSA EA (Principal)</p>
    <div class="body-copy">
      <p>I have a Masters' Degree in accounting and am an QDX Enrolled Agent. I am also a LedgerBooks Advanced Certified Consultant in both the online and desktop products including Enterprise and Point of Sale.<br>I provide individual and small business tax services, Accounting, bookkeeping, QDX representation, insurance audit representation, business license assistance and more.</p>
      <p>I have experience working with a wide variety of clients from the point where they first decide they want to start a business. They are often unsure about what to do first- I have a lot of experience to offer you.</p>
    </div>
  </div>
  <p class="layer quote">What a joy it is to watch success in action!</p>

  <div class="layer brand brand--cover">
    <span class="brand__dot"></span>
    <span class="brand__name">BLUECREST ACCOUNTING<br>&amp; CONSULTING, LLC</span>
  </div>

  <div class="layer contacts">
    <div class="contact">
      <svg viewBox="0 0 14 14"><circle cx="7" cy="7" r="7" fill="#c8202f"/><path d="M4.6 3.6l1.3 1.4-.7 1c.5 1 1.2 1.7 2.2 2.2l1-.7 1.4 1.3-.8 1.1C6.6 9.7 4.3 7.4 3.6 4.4z" fill="#fff"/></svg>
      <span>(555)014-2231</span>
    </div>
    <div class="contact">
      <svg viewBox="0 0 14 14"><circle cx="7" cy="7" r="7" fill="#c8202f"/><rect x="3.5" y="6" width="7" height="4" rx=".8" fill="#fff"/><rect x="5" y="3.8" width="4" height="2.6" fill="#fff"/></svg>
      <span>(555)019-7740</span>
    </div>
    <div class="contact">
      <svg viewBox="0 0 14 14"><circle cx="7" cy="7" r="7" fill="#c8202f"/><rect x="3.5" y="4.5" width="7" height="5" fill="#fff"/><path d="M3.5 4.5L7 7.5l3.5-3" stroke="#c8202f" stroke-width=".8" fill="none"/></svg>
      <span>office@bluecrestacct.com</span>
    </div>
    <div class="contact">
      <svg viewBox="0 0 14 14"><circle cx="7" cy="7" r="7" fill="#c8202f"/><path d="M7 3a2.6 2.6 0 0 1 2.6 2.6C9.6 7.6 7 11 7 11S4.4 7.6 4.4 5.6A2.6 2.6 0 0 1 7 3z" fill="#fff"/><circle cx="7" cy="5.6" r="1" fill="#c8202f"/></svg>
      <span>Bluecrest Accounting &amp; Consulting, LLC<br>2870 Maple Ridge Rd, PO Box 41<br>Fairlow, VA 20000</span>
    </div>
  </div>

  <div class="layer brand brand--front">
    <span class="brand__dot"></span>
    <span class="brand__name">BLUECREST ACCOUNTING<br>&amp; CONSULTING, LLC</span>
  </div>
  <div class="layer badge" aria-hidden="true"></div>
  <div class="layer cta">
    <h1 class="heading cta__title">LET US HELP YOU</h1>
    <span class="cta__bar">TO PREPARE YOUR INCOME TAX</span>
    <p class="web">www.bluecrestacct.com</p>
  </div>
</section>

<!-- Inside spread -->
<section class="spread spread--inside">
  <div class="panel panel--1">
    <div class="photo" role="img" aria-label="Photo of a businesswoman working with a calculator and binder at a desk" style="left:0;top:0;width:266.67px;height:280px;background:linear-gradient(135deg,#f2f3f4 0%,#d6d9dd 50%,#8b8f96 100%)"></div>
  </div>
  <div class="panel panel--2">
    <div class="photo" role="img" aria-label="Photos of a calculator with a help note and a hand pointing at bar charts" style="left:0;top:240px;width:266.67px;height:330px;background:linear-gradient(170deg,#dfe4ea 0%,#b9c6d6 45%,#6f8aa8 100%)"></div>
  </div>
  <div class="panel panel--3" style="background:var(--blue)"></div>

  <svg class="swooshes" viewBox="0 0 800 570" aria-hidden="true">
    <path d="M533,312 C615,358 700,392 800,400 L800,570 L533,570 Z" fill="#ffffff"/>
    <path d="M0,262 C190,208 400,246 533,300 C620,340 720,380 800,388 L800,400 C710,392 615,360 530,322 C400,266 190,228 0,282 Z" fill="#ffffff"/>
    <path d="M0,258 C190,200 400,236 533,290 C620,330 720,368 800,378 L800,392 C710,384 615,350 530,312 C400,258 190,220 0,274 Z" fill="#0054aa"/>
    <path d="M0,284 C190,232 400,270 530,326 C615,364 710,396 800,404" stroke="#c8202f" stroke-width="5" fill="none"/>
    <line x1="266.67" y1="0" x2="266.67" y2="570" stroke="rgba(0,0,0,.06)"/>
    <line x1="533.33" y1="0" x2="533.33" y2="570" stroke="rgba(0,0,0,.06)"/>
  </svg>

  <div class="layer why">
    <h2 class="heading why__title">TAX PREPARATION –<br><span>WHY HIRE US?</span></h2>
    <div class="body-copy">
      <p>Preparing your own income tax return can be a task that leaves you with more questions than answers. According to a study released by the US Government's Federal Review Office last year, most taxpayers (77% of 71 million taxpayers) believe they benefited from using a professional tax preparer.</p>
      <p>Whether we like it or not, today's tax laws are so complicated that filing a relatively simple return can be confusing. It is just too easy to overlook deductions and credits to which you are entitled. Even if you use a computer software program there's no substitute for the assistance of an experienced tax professional.</p>
    </div>
  </div>

  <div class="layer mess-header">
    <h2 class="heading">BOOKS A MESS:<br>NO PROBLEM!</h2>
  </div>
  <div class="layer mess">
    <p class="mess__lead">If you own a small business and haven't kept up your bookkeeping, don't worry.</p>
    <h3 class="heading mess__title">WE CAN HELP YOU.</h3>
    <p class="body-copy" style="font-size:9px">We'll prepare your bookkeeping for the year, prepare a full Schedule C, as well as your personal income tax return. Then we'll help you set up an easy system that allows you to keep your books in tip-top shape next year.</p>
  </div>

  <div class="layer gets">
    <h2 class="heading gets__title">HERE'S WHAT<br>YOUR GET...</h2>
    <ul>
      <li>Your tax return will be checked and rechecked by our computer software identifying potential problems the QDX may look at more closely and reviewing the math to limit QDX contacts.</li>
      <li>Your tax return can be filed electronically so you will get a refund back quicker.</li>
      <li>Our staff will show you how to adjust your payroll withholding to get more money back each week. Why give the QDX an interest free loan for up to 16 months.</li>
      <li>We will show you potential deductions to limit your tax liability for next year. In addition, we will give you a sheet of commonly overlooked deductions to limit the following year's tax liability.</li>
    </ul>
  </div>

  <div class="layer brand brand--back">
    <span class="brand__dot"></span>
    <span class="brand__name">BLUECREST ACCOUNTING<br>&amp; CONSULTING, LLC</span>
  </div>
  <p class="layer web web--back">www.bluecrestacct.com</p>
</section>

</body>
</html>
```